I need a newspaper ads that suits events / outings all over the world. refreshing feeling that suits my company logo.
Size of the ads is 6cm by 6cm a square
takenote
1) Joining up as members is free .
2) Places of interest tickets discount for members
3) Special events / outings host almost everyday
4) main point is everyone able to know each another
website : www.WandermoorHub.com
Target Market(s)
Targeting general age 18-40 . mainly singles
contents to put inside the ads
2) Local Places of interest tickets discount for members
4) Website : www.WandermoorHub.com
5) We also host photos contest
6) Meet the different faces of the world
7) Experience Sharing Gathering !
Industry/Entity Type
It Company
Requirements
Must have
- Refreshing feeling , and professional . will be uploading more pictures , kindly put some pictures combine into it to make people feel there is a lot activities can be involve when they join as member.

```html
<!DOCTYPE html>
<html lang="en">
<head>
<meta charset="utf-8">
<title>Gate to the New World – Wandermoor Events</title>
<link href="https://fonts.googleapis.com/css2?family=PT+Sans:ital,wght@0,400;0,700;1,400;1,700&display=swap" rel="stylesheet">
<style>
  :root{
    --ink-blue:#1d5f8f;
    --title-blue:#1a6fa6;
    --bright-blue:#2a87c6;
    --ribbon-blue:#2470b3;
    --band-blue:#1b5784;
    --footer-blue:#1f5f8c;
    --panel-top:#f4f5f6;
    --panel-bottom:#d9dcdf;
    --paper:#f6f2df;
    --badge-red:#c8161d;
    --badge-yellow:#ffd21f;
    --white:#ffffff;
    --swoosh:#b9bdc2;
  }
  *{box-sizing:border-box;margin:0;padding:0}
  html,body{width:1200px;height:1200px;overflow:hidden;background:#fff}
  .ad{position:relative;width:1200px;height:1200px;overflow:hidden;font-family:"PT Sans",Arial,sans-serif;color:var(--ink-blue)}

  /* top scene */
  .scene{position:absolute;left:0;top:0;width:1200px;height:643px;
    background:linear-gradient(180deg,#a9d6ef 0%,#d8eef8 28%,#5fc0d6 38%,#2aa4c4 46%,#7cc9c9 52%,#b08a63 58%,#9b7552 100%)}
  .headline{position:absolute;left:420px;top:44px;line-height:1}
  .headline .gate{font-weight:700;font-size:64px;color:var(--title-blue);letter-spacing:-1px}
  .headline .to-the{font-weight:700;font-size:38px;color:var(--white);margin-left:6px}
  .headline .new-world{display:block;font-weight:700;font-size:112px;color:var(--title-blue);letter-spacing:-3px;margin-top:-6px}
  .tagline{position:absolute;right:110px;top:204px;font-size:29px;color:var(--white)}

  .snapshot{position:absolute;background:var(--paper);padding:14px 14px 30px;box-shadow:2px 4px 10px rgba(0,0,0,.35)}
  .snapshot .photo{width:100%;height:100%}
  .snap-1{left:8px;top:330px;width:246px;height:218px;transform:rotate(-2deg)}
  .snap-1 .photo{background:linear-gradient(160deg,#6d8a4f,#a7b67c 60%,#e4ddd2)}
  .snap-2{left:298px;top:315px;width:196px;height:238px;transform:rotate(3deg)}
  .snap-2 .photo{background:linear-gradient(180deg,#2a1a14,#8a5b22 55%,#c9952e)}
  .snap-3{left:598px;top:334px;width:248px;height:216px;transform:rotate(2deg)}
  .snap-3 .photo{background:linear-gradient(170deg,#3c4a3d,#7e8a86 55%,#2a3340)}
  .snap-4{left:900px;top:314px;width:258px;height:226px;transform:rotate(9deg)}
  .snap-4 .photo{background:linear-gradient(170deg,#6aa6bf,#b9d3dc 55%,#8b6f5c)}

  /* divider band + ribbon */
  .band{position:absolute;left:0;top:636px;width:1200px;height:10px;background:var(--band-blue);z-index:2}
  .ribbon{position:absolute;left:636px;top:614px;width:516px;height:56px;background:var(--ribbon-blue);z-index:5;
    border:3px solid var(--white);box-shadow:0 3px 6px rgba(0,0,0,.3);
    font-style:italic;font-size:32px;color:var(--white);text-align:center;line-height:48px;white-space:nowrap}
  .ribbon b{font-weight:700}

  /* lower panel */
  .panel{position:absolute;left:0;top:646px;width:1200px;height:480px;z-index:1;background:linear-gradient(180deg,var(--panel-top),var(--panel-bottom))}
  .swoosh{position:absolute;left:0;top:0}
  .benefit{position:absolute;white-space:nowrap;color:var(--ink-blue);font-size:30px;line-height:1}
  .benefit em{font-style:italic;color:var(--title-blue)}
  .benefit .big{font-size:50px;letter-spacing:-1px}
  .benefit-free{left:93px;top:30px}
  .benefit-free em{font-size:44px}
  .benefit-tickets{left:254px;top:94px}
  .benefit-events{left:127px;top:164px}
  .benefit-events .big{font-size:46px}
  .benefit-faces{left:322px;top:216px}
  .benefit-faces .small{font-style:italic}
  .benefit-know{left:313px;top:286px}
  .benefit-know .small{font-style:italic}
  .benefit-social{left:406px;top:344px}
  .benefit-social .small{font-style:italic}

  .badge{position:absolute;left:870px;top:70px;width:240px;height:240px}
  .badge-text{position:absolute;left:870px;top:70px;width:240px;height:240px;transform:rotate(-22deg);
    text-align:center;color:var(--badge-yellow);font-weight:400}
  .badge-text .label{display:block;margin-top:62px;font-size:32px;line-height:1}
  .badge-text .value{display:block;font-size:70px;font-weight:700;line-height:1;margin-top:2px}

  .brand{position:absolute;left:70px;top:354px;display:flex;align-items:center;gap:12px}
  .brand-dot{width:44px;height:44px;border-radius:50%;background:var(--ink-blue)}
  .brand-name{font-size:27px;font-weight:700;color:var(--ink-blue);line-height:1.05}

  /* footer */
  .footer{position:absolute;left:0;top:1126px;width:1200px;height:74px;background:var(--footer-blue);z-index:3;
    color:var(--white);font-size:30px;display:flex;align-items:center}
  .contact{position:absolute;display:flex;align-items:center;gap:20px}
  .contact-email{left:40px}
  .contact-web{left:704px}
</style>
</head>
<body>
<main class="ad">
  <section class="scene" role="img" aria-label="Resort terrace with wooden deck and pool overlooking a turquoise sea, palm leaves at the edges">
    <h1 class="headline"><span class="gate">GATE</span><span class="to-the">to the</span><span class="new-world">NEW WORLD</span></h1>
    <p class="tagline">Meet with Happiness!</p>

    <figure class="snapshot snap-1"><div class="photo" role="img" aria-label="Member feeding a giraffe at a zoo"></div></figure>
    <figure class="snapshot snap-2"><div class="photo" role="img" aria-label="Traditional dancers in golden costumes on stage"></div></figure>
    <figure class="snapshot snap-3"><div class="photo" role="img" aria-label="Group of young friends posing together on an outing"></div></figure>
    <figure class="snapshot snap-4"><div class="photo" role="img" aria-label="Couple embracing by the sea"></div></figure>
  </section>

  <div class="band"></div>

  <section class="panel">
    <svg class="swoosh" width="1200" height="480" viewBox="0 0 1200 480" aria-hidden="true">
      <path d="M520 470 C760 360 980 320 1200 330 L1200 380 C1000 360 780 400 560 480 Z" fill="var(--swoosh)" opacity=".55"/>
      <path d="M660 480 C860 410 1040 390 1200 400 L1200 430 C1050 420 880 440 720 480 Z" fill="var(--swoosh)" opacity=".35"/>
    </svg>

    <p class="benefit benefit-free"><em>Free</em> Membership!</p>
    <p class="benefit benefit-tickets">Tickets <em class="big">Discount for Members</em></p>
    <p class="benefit benefit-events">Special <em class="big">Events / Outings</em> everyday!</p>
    <p class="benefit benefit-faces"><span class="small">Different</span> <em class="big">Faces of the World</em></p>
    <p class="benefit benefit-know"><span class="small">Know</span> <em class="big">Each Other!</em></p>
    <p class="benefit benefit-social"><span class="small">Friendship, Sharing,</span> <em class="big">Social Gathering</em></p>

    <svg class="badge" viewBox="0 0 250 250" aria-hidden="true">
      <defs>
        <radialGradient id="badgeFill" cx="45%" cy="40%" r="60%">
          <stop offset="0" stop-color="#e8232a"/>
          <stop offset="1" stop-color="#c8161d"/>
        </radialGradient>
      </defs>
      <polygon fill="url(#badgeFill)" points="125,5 145,27 172,14 180,43 210,42 206,72 234,84 218,109 240,130 214,146 226,174 196,179 192,209 163,203 148,230 125,210 102,230 87,203 58,209 54,179 24,174 36,146 10,130 32,109 16,84 44,72 40,42 70,43 78,14 105,27"/>
    </svg>
    <div class="badge-text"><span class="label">Discount<br>Upto</span><span class="value">35%</span></div>

    <div class="brand">
      <span class="brand-dot"></span>
      <span class="brand-name">WANDERMOOR<br>EVENTS</span>
    </div>
  </section>

  <div class="ribbon">We also host <b>PHOTO CONTEST</b></div>

  <footer class="footer">
    <div class="contact contact-email">
      <svg width="40" height="28" viewBox="0 0 40 28" aria-hidden="true">
        <rect x="1" y="1" width="38" height="26" fill="var(--white)"/>
        <path d="M1 1 L20 16 L39 1" fill="none" stroke="var(--footer-blue)" stroke-width="3"/>
      </svg>
      <span>Enquires@wandermoorhub.com</span>
    </div>
    <div class="contact contact-web">
      <svg width="32" height="32" viewBox="0 0 32 32" aria-hidden="true">
        <circle cx="16" cy="16" r="14" fill="var(--white)"/>
        <path d="M10 8 q5 2 4 7 q-3 2 -2 7 M20 6 q-2 5 3 7 q4 1 3 6" fill="none" stroke="var(--footer-blue)" stroke-width="3"/>
      </svg>
      <span>www.WandermoorHub.com</span>
    </div>
  </footer>
</main>
</body>
</html>
```